New Business Card for Odd Bit Designs

I create and make jewellery and Clothing. But when it comes to business card design I fail completely.

Sketching is my area, drawing, putting things together neatly, not so much.

Here is a little blurb about my company:

Odd Bit Designs is a truly unique customer experience. Work one on one with Owner Marla Pemberton to make your costuming dreams come true.

Not after a costume? Browse through the store for a look at beautiful and unique piece of jewellery. Each piece has been put together by Marla, by hand. You'll find Steampunk, gothic, lolita and other quirky styles.

Want something else? What abotu a pair of warm kitty paws? A Pair of Kitty ears? A pony tail to wear on your jeans? There are so many options and things to choose! You will want to take it all home.

I have attached the previous business card with my mascot "Greta" As you can see there is a very Greta of Cloudmere feel to the overall company, with references to The Lost Tinker, and the idea that "We are all made here".

Colour's to use would be purple and blue. The winning design would show the unique but professional approach that Odd Bit Designs takes when creating each piece for their customers.

Reason: Wanted to give you a chance to go over feed back that has been sent out. I am committed to paying for the design that I will use. I think another week will help tweak things up.

Nerds, Geeks and Sci-Fi people aged 20 - 34 both Male and Female

Store

• Website address: www.oddbitdesigns.net

Yeah, rest is up too you!
• Honestly, if you could make the whole thing look like a Hugh Pellbrook "Greta of Cloudmere" Drawing with the same line working style that would be amazing!

But I won't restrict you! I'd like to see what you can come up with.

```html
<!DOCTYPE html>
<html lang="en">
<head>
<meta charset="utf-8">
<title>Odd Bit Designs – Business Card</title>
<link rel="stylesheet" href="https://fonts.googleapis.com/css2?family=Fira+Sans:wght@400;500;600&family=Alegreya+SC:wght@500&display=swap">
<style>
  :root {
    --stage: #e6e6ea;
    --card: #fbfbfc;
    --card-shade: #eceef2;
    --band-purple: #3e3bb0;
    --band-purple-light: #6a5fd2;
    --band-blue: #1d4f8c;
    --band-blue-light: #3f79b8;
    --brand-purple: #5a3a92;
    --brand-blue: #3a8fd3;
    --ink: #2b2b2f;
    --mascot-top: #3c3a66;
    --mascot-mid: #5b63c4;
    --mascot-low: #3f78c4;
  }
  * { box-sizing: border-box; margin: 0; padding: 0; }
  html, body {
    width: 1200px; height: 861px; overflow: hidden;
    background: var(--stage);
    font-family: "Fira Sans", Arial, sans-serif;
    color: var(--ink);
  }
  .stage { position: relative; width: 1200px; height: 861px; }
  .card {
    position: absolute; top: 254px;
    width: 560px; height: 352px;
    background: linear-gradient(160deg, var(--card) 0%, var(--card-shade) 100%);
    box-shadow: 0 10px 28px rgba(0,0,0,.18);
    overflow: hidden;
  }
  .card--front { left: 25px; }
  .card--back { left: 615px; }
  .band { position: absolute; left: 0; width: 100%; display: block; }
  .band--top { top: 0; height: 40px; }
  .band--bottom { bottom: 0; height: 30px; }

  .mascot {
    position: absolute;
    background: linear-gradient(180deg, var(--mascot-top) 0%, var(--mascot-mid) 45%, var(--mascot-low) 100%);
    border-radius: 40% 40% 12% 12% / 30% 30% 10% 10%;
    opacity: .85;
  }
  .card--front .mascot { left: 22px; top: 58px; width: 240px; height: 250px; }
  .card--back .mascot { left: 12px; top: 62px; width: 160px; height: 156px; }

  .wordmark {
    font-family: "Fira Sans", Arial, sans-serif;
    font-weight: 500;
    color: var(--brand-purple);
    letter-spacing: .14em;
    line-height: 1;
    text-transform: uppercase;
  }
  .card--front .wordmark {
    position: absolute; right: 40px; top: 60px; text-align: right; font-size: 38px;
  }
  .card--back .wordmark {
    position: absolute; left: 14px; top: 234px; font-size: 23px; text-align: left;
  }
  .wordmark span { display: block; }
  .wordmark span + span { margin-top: 6px; }

  .offer {
    position: absolute; right: 40px; top: 158px; text-align: right;
    font-family: "Alegreya SC", Georgia, serif; font-weight: 500;
    font-size: 11.5px; line-height: 1.3; color: var(--ink); letter-spacing: .02em;
  }
  .owner {
    position: absolute; right: 40px; top: 196px;
    font-size: 31px; font-weight: 600; line-height: 1.2; color: var(--brand-purple);
  }
  .contacts {
    position: absolute; right: 40px; top: 244px; list-style: none;
    text-align: right; font-size: 15px;
  }
  .contacts li { display: flex; justify-content: flex-end; align-items: center; gap: 8px; height: 30px; }
  .contacts svg { width: 22px; height: 22px; flex: none; }

  .blurb {
    position: absolute; left: 190px; top: 56px; width: 330px;
    font-size: 13.5px; line-height: 1.22;
  }
  .blurb p + p { margin-top: 8px; }
  .blurb .lead { color: var(--brand-purple); font-weight: 600; }
  .blurb .owner-name { color: var(--brand-blue); font-weight: 600; }
</style>
</head>
<body>
<main class="stage">

  <section class="card card--front" aria-label="Business card front">
    <svg class="band band--top" viewBox="0 0 560 46" preserveAspectRatio="none" aria-hidden="true">
      <defs>
        <linearGradient id="purpleBandFront" x1="0" x2="1">
          <stop offset="0" stop-color="var(--band-purple)"/>
          <stop offset="1" stop-color="var(--band-purple-light)"/>
        </linearGradient>
      </defs>
      <path d="M0 0H560V18C520 22 500 14 460 20C420 26 380 16 330 22C280 30 240 18 190 26C150 32 110 24 70 34C40 40 20 30 0 38Z" fill="url(#purpleBandFront)"/>
    </svg>

    <div class="mascot" role="img" aria-label="Mascot illustration of Greta, a girl in a top hat sitting on the floor"></div>

    <h1 class="wordmark"><span>Odd Bit</span><span>Designs</span></h1>
    <p class="offer">Steampunk Jewellery • Kitty Ears • Paws<br>Tails • Custom Costumes • Lolita</p>
    <h2 class="owner">Marla Pemberton</h2>
    <ul class="contacts">
      <li>hello.oddbit@mailbay.net
        <svg viewBox="0 0 24 24" aria-hidden="true"><circle cx="12" cy="12" r="10.5" fill="none" stroke="var(--brand-purple)" stroke-width="1.8"/><rect x="6.5" y="8.5" width="11" height="7.5" rx="1" fill="none" stroke="var(--brand-purple)" stroke-width="1.5"/><path d="M6.8 9L12 13L17.2 9" fill="none" stroke="var(--brand-purple)" stroke-width="1.5"/></svg>
      </li>
      <li>www.oddbitdesigns.net
        <svg viewBox="0 0 24 24" aria-hidden="true"><circle cx="12" cy="12" r="10.5" fill="none" stroke="var(--brand-purple)" stroke-width="1.8"/><rect x="6.5" y="7.5" width="11" height="7.5" rx="1" fill="none" stroke="var(--brand-purple)" stroke-width="1.5"/><path d="M10 17H14M12 15V17" stroke="var(--brand-purple)" stroke-width="1.5"/></svg>
      </li>
    </ul>

    <svg class="band band--bottom" viewBox="0 0 560 40" preserveAspectRatio="none" aria-hidden="true">
      <defs>
        <linearGradient id="blueBandFront" x1="0" x2="1">
          <stop offset="0" stop-color="var(--band-blue-light)"/>
          <stop offset="1" stop-color="var(--band-blue)"/>
        </linearGradient>
      </defs>
      <path d="M0 14C40 8 80 16 130 10C190 4 240 14 300 8C360 2 420 12 480 6C520 2 540 8 560 4V40H0Z" fill="url(#blueBandFront)"/>
    </svg>
  </section>

  <section class="card card--back" aria-label="Business card back">
    <svg class="band band--top" viewBox="0 0 560 46" preserveAspectRatio="none" aria-hidden="true">
      <defs>
        <linearGradient id="purpleBandBack" x1="0" x2="1">
          <stop offset="0" stop-color="var(--band-purple)"/>
          <stop offset="1" stop-color="var(--band-purple-light)"/>
        </linearGradient>
      </defs>
      <path d="M0 0H560V16C520 22 490 12 450 20C410 28 370 16 320 24C270 30 230 18 180 26C140 32 100 22 60 32C35 38 15 30 0 36Z" fill="url(#purpleBandBack)"/>
    </svg>

    <div class="mascot" role="img" aria-label="Small mascot illustration of Greta in a top hat, seated"></div>

    <p class="wordmark"><span>Odd Bit</span><span>Designs</span></p>

    <div class="blurb">
      <p><span class="lead">ODD BIT DESIGNS</span> is a truly unique customer experience. Work one on one with Owner <span class="owner-name">Marla Pemberton</span> to make your dreams come true.</p>
      <p><span class="lead">Browse through the store</span> and look for a beautiful and unique piece of jewellery. Put together by hand in the Odd Bit Studio. You'll discover Steampunk, Gothic and Lolita pieces among many other quirky designs.</p>
      <p><span class="lead">Want something else?</span> What about a pair of warm kitty paws? A Pair of Kitty ears? A pony tail to wear on your jeans? There are so many options and things to choose!</p>
      <p>You will want to take it all home.</p>
    </div>

    <svg class="band band--bottom" viewBox="0 0 560 40" preserveAspectRatio="none" aria-hidden="true">
      <defs>
        <linearGradient id="blueBandBack" x1="0" x2="1">
          <stop offset="0" stop-color="var(--band-blue-light)"/>
          <stop offset="1" stop-color="var(--band-blue)"/>
        </linearGradient>
      </defs>
      <path d="M0 12C50 6 90 16 140 10C200 4 250 14 310 8C370 2 430 12 490 6C525 3 545 8 560 5V40H0Z" fill="url(#blueBandBack)"/>
    </svg>
  </section>

</main>
</body>
</html>
```